Building Company Business Card Design

I am looking to get a business card designed for my Building Company. Please find the logo attached.

Industry/Entity Type

Business

Contact Information for Business Card

Mobile 0472 913 706
Email admin@harbourlineconstruct.com.au
Website www.harbourlineconstruct.com.au

Colors
0255a3

```html
<!DOCTYPE html>
<html lang="en">
<head>
<meta charset="utf-8">
<title>Harbourline Construct – Business Card</title>
<link href="https://fonts.googleapis.com/css2?family=Montserrat:wght@500;600&display=swap" rel="stylesheet">
<style>
  :root {
    --brand-blue: #0255a3;
    --deep-blue: #0d3f86;
    --paper: #ffffff;
    --stage-top: #1c1c1c;
    --stage-bottom: #4e4e4e;
  }
  * { box-sizing: border-box; margin: 0; padding: 0; }
  html, body { width: 1200px; height: 1200px; overflow: hidden; }
  body {
    background: linear-gradient(180deg, var(--stage-top), var(--stage-bottom));
    font-family: "Montserrat", sans-serif;
    position: relative;
  }
  .card {
    position: absolute;
    left: 250px;
    width: 700px;
    height: 400px;
    background: var(--paper);
    box-shadow: 0 12px 30px rgba(0,0,0,0.35);
    overflow: hidden;
  }
  .card--front { top: 150px; }
  .card--back { top: 650px; }
  .wordmark {
    position: absolute;
    color: var(--brand-blue);
    font-weight: 600;
    letter-spacing: 1px;
    white-space: nowrap;
  }
  .card--front .wordmark {
    left: 0; right: 0; top: 178px;
    text-align: center;
    font-size: 34px;
  }
  .card--back .wordmark {
    left: 60px; top: 110px;
    font-size: 26px;
  }
  .card__curves { position: absolute; inset: 0; }
  .contact {
    position: absolute;
    right: 40px;
    top: 150px;
    text-align: right;
    color: var(--paper);
    font-weight: 500;
  }
  .contact__name { font-size: 22px; font-weight: 600; letter-spacing: 0.5px; line-height: 28px; }
  .contact__role { font-size: 15px; line-height: 20px; margin-bottom: 34px; }
  .contact__line {
    font-size: 15px;
    line-height: 28px;
    display: flex;
    justify-content: flex-end;
    align-items: center;
    gap: 8px;
  }
  .contact__line svg { width: 15px; height: 15px; flex: none; }
</style>
</head>
<body>

<section class="card card--front">
  <div class="wordmark">Harbourline Construct</div>
</section>

<section class="card card--back">
  <svg class="card__curves" viewBox="0 0 700 400" preserveAspectRatio="none">
    <path d="M0,220 C250,300 500,200 540,0 L700,0 L700,400 L0,400 Z" fill="var(--brand-blue)"/>
    <path d="M575,0 C540,150 420,240 300,272" fill="none" stroke="var(--deep-blue)" stroke-width="24" opacity="0.45"/>
    <path d="M0,244 C262,322 528,214 568,0" fill="none" stroke="var(--paper)" stroke-width="6"/>
  </svg>

  <div class="wordmark">Harbourline Construct</div>

  <div class="contact">
    <div class="contact__name">JOHN DOE</div>
    <div class="contact__role">Director</div>
    <div class="contact__line">0472 913 706
      <svg viewBox="0 0 24 24" fill="#fff"><path d="M6.6 10.8a15.1 15.1 0 0 0 6.6 6.6l2.2-2.2a1 1 0 0 1 1-.25 11.4 11.4 0 0 0 3.6.57 1 1 0 0 1 1 1V20a1 1 0 0 1-1 1A17 17 0 0 1 3 4a1 1 0 0 1 1-1h3.5a1 1 0 0 1 1 1c0 1.25.2 2.45.57 3.57a1 1 0 0 1-.25 1z"/></svg>
    </div>
    <div class="contact__line">admin@harbourlineconstruct.com.au
      <svg viewBox="0 0 24 24" fill="#fff"><path d="M2 5h20v14H2z M3.5 6.5 12 13l8.5-6.5" stroke="var(--brand-blue)" stroke-width="1.5"/></svg>
    </div>
    <div class="contact__line">www.harbourlineconstruct.com.au
      <svg viewBox="0 0 24 24" fill="none" stroke="#fff" stroke-width="2"><circle cx="12" cy="12" r="9"/><path d="M3 12h18M12 3c3 3 3 15 0 18M12 3c-3 3-3 15 0 18"/></svg>
    </div>
  </div>
</section>

</body>
</html>
```